Customer Value Leaflet

We need a bi-fold brochure designing, based on the attached PDF wireframes. Our company name is quillbrookery.com (of which the logo is currently being designed). The corporate colour is orange (the exact shade of which we are happy to leave to the designers discretion).

The leaflet will distributed to customer experience experts and marketers so the design needs to be bright, engaging, clean and simple. Design is critical.

```html
<!DOCTYPE html>
<html lang="en">
<head>
<meta charset="utf-8">
<title>Customer Value Leaflet – Quillbrookery</title>
<link rel="stylesheet" href="https://fonts.googleapis.com/css2?family=Arimo:wght@400;700&family=Open+Sans:ital,wght@0,400;0,600;0,700;1,700&display=swap">
<style>
:root{
  --orange:#f39325;
  --orange-deep:#e8731a;
  --orange-text:#f08a24;
  --red:#d0272d;
  --red-dark:#b3222a;
  --yellow:#ffd200;
  --navy:#2f3a8f;
  --ink:#1e1e1e;
  --white:#ffffff;
  --frame:#4a4a4a;
}
*{box-sizing:border-box;margin:0;padding:0}
html,body{width:873px;height:1200px;overflow:hidden;background:var(--white)}
body{font-family:"Open Sans",Arial,sans-serif;color:var(--ink)}
.sheet{position:absolute;left:0;top:0;width:841px;height:1155px;transform:scale(1.038,1.039);transform-origin:0 0}
.panel{position:absolute;overflow:hidden;border:1.5px solid var(--frame)}
.pattern{position:absolute;inset:0;background:radial-gradient(circle at 30% 30%,var(--orange) 0%,var(--orange-deep) 140%)}
.abs{position:absolute}
.flip{position:absolute;inset:0;transform:rotate(180deg)}
.band{position:absolute;left:0;right:0;background:var(--red);color:var(--white);display:flex;align-items:center;justify-content:center;font-size:14px}

/* cover */
.brand{left:43px;top:32px;color:var(--yellow);font-size:12px}
.cover-title{left:0;width:380px;text-align:center;color:var(--white);font-family:"Arimo",Arial,sans-serif;font-weight:700;line-height:1}
.were{top:82px;font-family:"Open Sans",Arial,sans-serif;font-style:italic;font-size:24px}
.customer{top:128px;font-size:62px;letter-spacing:1px}
.value{top:205px;font-size:62px}
.company-row{left:50px;right:56px;top:298px;display:flex;align-items:center;gap:14px;color:var(--white);font-family:"Arimo",Arial,sans-serif;font-weight:700;font-size:20px}
.company-row .bar{height:5px;background:var(--white);flex:1}

/* intro */
.intro-text{left:13px;top:44px;width:198px;height:250px;background:rgba(255,255,255,.82);padding:6px 8px;font-family:"Arimo",Arial,sans-serif;font-size:15px;line-height:1.3}
.intro-text p+p{margin-top:16px}
.image-slot{left:218px;top:44px;width:184px;height:248px;background:var(--red);color:var(--white);display:flex;align-items:center;justify-content:center;text-align:center;font-size:14px;line-height:1.4;padding:0 20px}

/* clv panel */
.clv-card{top:72px;height:78px;display:flex}
.clv-card .who{width:36px;background:var(--white);writing-mode:vertical-rl;display:flex;align-items:center;justify-content:center;font-size:14px}
.clv-card .amount{flex:1;background:var(--red-dark);color:var(--white);font-size:24px;line-height:1.2;display:flex;align-items:center;justify-content:center;text-align:center;padding:0 8px}
.benefit{top:160px;width:153px;height:124px;background:var(--white);color:var(--orange-text);font-size:13px;line-height:1.35;text-align:center;display:flex;align-items:center;justify-content:center;padding:0 6px}
.optimise-arrow{left:172px;top:52px;width:62px;height:225px}
.optimise-label{left:188px;top:60px;width:30px;height:180px;writing-mode:vertical-rl;color:var(--white);font-size:12.5px;display:flex;align-items:center;justify-content:center;letter-spacing:.3px}
.science{left:24px;top:305px;width:360px;color:var(--navy);font-size:12.5px;line-height:1.3;text-align:center}

/* meet */
.persona-head{top:24px;width:160px;height:28px;background:var(--red);color:var(--white);font-size:15px;display:flex;align-items:center;justify-content:center}
.persona-card{top:52px;width:160px;height:266px;background:var(--white);text-align:center;font-weight:700;font-size:12.5px;line-height:1.45;padding:0 6px}
.persona-figure{width:62px;height:105px;margin:14px auto 14px;border-radius:30px 30px 8px 8px;background:linear-gradient(#bdbdbd,#e5e5e5)}

/* journey */
.journey-col{top:8px;height:375px;background:var(--white)}
.step{position:absolute;left:0;right:0;text-align:center;font-weight:700;font-size:12.5px;line-height:1.4;padding:0 4px}
.icon-slot{position:absolute;left:50%;width:48px;height:44px;margin-left:-24px;border-radius:10px;background:linear-gradient(#9a9a9a,#d0d0d0)}
.time-tab{left:186px;width:36px;background:var(--red);color:var(--white);writing-mode:vertical-rl;transform:rotate(180deg);display:flex;align-items:center;justify-content:center;font-size:13px}

/* close */
.promise{color:var(--white);font-weight:700;font-size:20px;line-height:1.5}
.promise u{text-decoration-thickness:2px}
</style>
</head>
<body>
<div class="sheet">

  <!-- Cover (folded, printed upside down) -->
  <section class="panel" style="left:2px;top:2px;width:408px;height:384px">
    <div class="pattern" role="img" aria-label="Orange damask pattern background"></div>
    <div class="flip">
      <div class="abs brand">[Quillbrookery]</div>
      <div class="abs cover-title were">We’re a</div>
      <div class="abs cover-title customer">CUSTOMER</div>
      <div class="abs cover-title value">VALUE</div>
      <div class="abs company-row"><span class="bar"></span>company<span class="bar"></span></div>
    </div>
  </section>

  <!-- Intro -->
  <section class="panel" style="left:2px;top:385px;width:408px;height:386px">
    <div class="pattern" role="img" aria-label="Orange damask pattern background"></div>
    <div class="abs intro-text">
      <p>Veyra is our Customer Value Platform, designed for Marketers in the Digital Enterprise.</p>
      <p>Veyra is like having a team of data scientists making valuable insights available to your website in real-time so you can deliver the ultimate customer experience</p>
    </div>
    <div class="abs image-slot" role="img" aria-label="Data science or customer experience image">Image Here (Data Science related and / or Customer Experience)</div>
    <div class="band" style="top:342px;height:43px">quillbrookery.com &nbsp;&nbsp;|&nbsp;&nbsp; 0845 000 3172</div>
  </section>

  <!-- CLV (folded, printed upside down) -->
  <section class="panel" style="left:2px;top:770px;width:408px;height:385px">
    <div class="pattern" role="img" aria-label="Orange damask pattern background"></div>
    <div class="flip">
      <div class="band" style="top:0;height:52px;font-size:15px">Once you can calculate CLV…</div>
      <div class="abs clv-card" style="left:33px;width:137px"><span class="who">Kim</span><span class="amount">CLV of £149</span></div>
      <div class="abs clv-card" style="left:233px;width:135px"><span class="who">Kevin</span><span class="amount">CLV of £282</span></div>
      <svg class="abs optimise-arrow" viewBox="0 0 62 225" aria-hidden="true"><path d="M16 0H46V190H62L31 225L0 190H16Z" fill="var(--red)"/></svg>
      <div class="abs optimise-label">OPTIMISE YOUR MARKETING</div>
      <div class="abs benefit" style="left:33px">you can personalise Kim’s marketing experience to grow her lifetime value to be more like Kevin’s</div>
      <div class="abs benefit" style="left:235px;width:133px">you can understand why Kevin is more valuable and acquire more customers like him</div>
      <p class="abs science">We use data and science to <b>predict how your customers will behave in future</b>. Even if you already use CLV we can help you do and earn more… <b>quillbrookery.com</b></p>
    </div>
  </section>

  <!-- Meet Kim & Kevin -->
  <section class="panel" style="left:430px;top:2px;width:410px;height:384px">
    <div class="pattern" role="img" aria-label="Orange damask pattern background"></div>
    <div class="abs persona-head" style="left:38px">MEET KIM</div>
    <div class="abs persona-card" style="left:38px">
      <div class="persona-figure" role="img" aria-label="Illustration of Kim"></div>
      Kim has purchased 3 items from you over the past 3 months @ £109 margin and you acquired her though a Searchly PPC campaign
    </div>
    <div class="abs persona-head" style="left:210px">MEET KEVIN</div>
    <div class="abs persona-card" style="left:210px">
      <div class="persona-figure" role="img" aria-label="Illustration of Kevin"></div>
      Kevin purchased an item last week @ £31 margin and you acquired him though a retargeting campaign
    </div>
    <div class="band" style="top:335px;height:48px;font-weight:700;font-size:13.5px">Right now you probably think Kim is your best customer…</div>
  </section>

  <!-- Journey -->
  <section class="panel" style="left:430px;top:385px;width:410px;height:386px">
    <div class="pattern" role="img" aria-label="Orange damask pattern background"></div>
    <div class="abs journey-col" style="left:24px;width:162px">
      <p class="step" style="top:14px">Kim calls you to return an item…</p>
      <div class="icon-slot" style="top:62px" role="img" aria-label="Headset icon"></div>
      <p class="step" style="top:124px">places 4 more online orders…</p>
      <div class="icon-slot" style="top:172px" role="img" aria-label="Shopping cart icon"></div>
      <p class="step" style="top:238px">then places another order but doesn’t come back for a month</p>
      <div class="icon-slot" style="top:312px" role="img" aria-label="Stop hand icon"></div>
    </div>
    <div class="abs journey-col" style="left:222px;width:168px">
      <p class="step" style="top:14px">Kevin makes another purchase…</p>
      <div class="icon-slot" style="top:62px" role="img" aria-label="Shopping basket icon"></div>
      <p class="step" style="top:116px">then 2 more (and even tweets about how great your service is)…</p>
      <div class="icon-slot" style="top:184px" role="img" aria-label="Social post icon"></div>
      <p class="step" style="top:238px">and continues to make purchases on a bi-monthly basis</p>
      <div class="icon-slot" style="top:312px" role="img" aria-label="Shopping cart icon"></div>
    </div>
    <div class="abs time-tab" style="top:18px;height:96px">+ 1 WEEK</div>
    <div class="abs time-tab" style="top:144px;height:96px">+ 1 MONTH</div>
    <svg class="abs" style="left:162px;top:242px" width="82" height="142" viewBox="0 0 82 142" aria-hidden="true"><path d="M24 0H60V78H82L41 120L0 78H24Z" fill="var(--red)"/></svg>
    <div class="abs" style="left:186px;top:246px;width:36px;height:80px;writing-mode:vertical-rl;transform:rotate(180deg);color:var(--white);font-size:13px;display:flex;align-items:center;justify-content:center">+ 6 MONTHS</div>
  </section>

  <!-- Close -->
  <section class="panel" style="left:430px;top:770px;width:410px;height:385px">
    <div class="pattern" role="img" aria-label="Orange damask pattern background"></div>
    <div class="band" style="top:0;height:46px;color:var(--yellow);font-weight:700;font-size:14px">but really it is Kevin.</div>
    <p class="abs promise" style="left:24px;top:130px;width:370px">By predicting <u>Customer Lifetime</u><br><u>Value</u> today…</p>
    <p class="abs promise" style="right:16px;top:194px;width:370px;text-align:right">…you can optimise<br>your business for tomorrow</p>
    <p class="abs" style="left:0;right:0;top:325px;text-align:center;color:var(--white);font-weight:700;font-size:17px">Find our more at www.quillbrookery.com</p>
  </section>

</div>
</body>
</html>
```